Business Card Design Project

We require a business card template to cover basic contact information - our company logo, names of employees, title, mobile and email.

Target Market(s)

Corporate

Industry/Entity Type

Business

Font styles to use
Sans Serif

Requirements
Nice to have
• Thinking it would be great just to have the logo taking up approximately half the space (so it goes as far across the top of the card as possible) and then contact details in the lower half of the card. Keen just to use only the two colours in the logo, on a white background.
Should not have
• No fussy drawings

```html
<!DOCTYPE html>
<html lang="en">
<head>
<meta charset="utf-8">
<title>Larkmere Developments – Business Card</title>
<link rel="stylesheet" href="https://fonts.googleapis.com/css2?family=Tinos:wght@400;700&display=swap">
<style>
  :root {
    --backdrop: #3b1d14;
    --card: #ffffff;
    --teal: #13a9b1;
    --navy: #1b6b99;
  }
  * { margin: 0; padding: 0; box-sizing: border-box; }
  html, body {
    width: 900px;
    height: 1200px;
    overflow: hidden;
    background: var(--backdrop);
  }
  .canvas {
    position: relative;
    width: 900px;
    height: 1200px;
    display: flex;
    align-items: center;
    justify-content: center;
  }
  .business-card {
    position: relative;
    width: 720px;
    height: 422px;
    background: var(--card);
    font-family: "Tinos", "Times New Roman", serif;
  }
  .brand {
    position: absolute;
    left: 56px;
    right: 56px;
    top: 96px;
    display: flex;
    align-items: center;
    gap: 22px;
  }
  .brand-mark {
    flex: none;
    width: 52px;
    height: 52px;
    background: var(--teal);
  }
  .brand-name {
    color: var(--navy);
    font-weight: 700;
    font-size: 48px;
    line-height: 1;
    white-space: nowrap;
  }
  .employee {
    position: absolute;
    left: 0;
    width: 666px;
    top: 248px;
    text-align: center;
    color: var(--navy);
    font-weight: 700;
    font-size: 33px;
    line-height: 46px;
  }
  .contact {
    position: absolute;
    left: 37px;
    top: 352px;
    font-size: 29px;
    color: var(--teal);
    white-space: nowrap;
  }
  .contact .label {
    color: var(--navy);
    font-weight: 700;
  }
</style>
</head>
<body>
  <main class="canvas">
    <article class="business-card">
      <header class="brand">
        <span class="brand-mark" aria-hidden="true"></span>
        <h1 class="brand-name">Larkmere Developments</h1>
      </header>
      <div class="employee">
        <p class="employee-name">Employee Name</p>
        <p class="employee-title">Title</p>
      </div>
      <p class="contact">
        <span class="label">Ph:</span> 123-456-7890
        <span class="label">Email:</span> Employee@lk.comm
      </p>
    </article>
  </main>
</body>
</html>
```